Modern furniture store needs a catalogue in PDF

We need a catalogue design for a company based in Ecuador, South America called KOVARI. We have replica furniture and also authentic furniture from Europe which are classified in two separate ranges. KOVARI is the brand for designer replicas and THE LUMENHAUS SHOP is for authentic designer furniture and house decoration. We would like to see a design that provides an idea of exclusivity and minimalistic design.

Target Market(s)

Upmarket families and new home owners from Ecuador, South America.

Industry/Entity Type

Furniture Store

Font styles to use
Sans Serif

Requirements
Must have
• A nice presentation of each furniture item.
• You can look for images on the internet for each product as they are designer items available all around the world. You can use images from the websites:
• www.kovari-home.net
• www.pelzora.com
• www.wimsel.fi
• The images don't need to be high resolution as the PDF will be sent electronically (i.e. via email) and not printed.
Nice to have
• Diagrams with the dimensions of each item so that clients understand how big they are.
• It could be in spanish, but I could also translate it after the design is finished.

```html
<!DOCTYPE html>
<html lang="es">
<head>
<meta charset="utf-8">
<title>KOVARI — Catálogo Sillonería</title>
<link href="https://fonts.googleapis.com/css2?family=Fira+Sans+Condensed:wght@300;400;600;700&display=swap" rel="stylesheet">
<style>
  :root {
    --backdrop: #8a8a8a;
    --paper: #ffffff;
    --ink: #1c1c1c;
    --rule: #222222;
    --label-bg: #d9d9d9;
    --dash: #c4c4c4;
    --side-title: #b9b9b9;
    --drawing: #f1f1f1;
    --swatch-negro: #111111;
    --swatch-blanco: #f2f2f2;
    --swatch-caffe: #5a4d47;
    --swatch-rojo: #c8202c;
  }
  * { box-sizing: border-box; margin: 0; padding: 0; }
  html, body { width: 1200px; height: 517px; overflow: hidden; }
  body {
    background: var(--backdrop);
    font-family: "Fira Sans Condensed", sans-serif;
    color: var(--ink);
    position: relative;
  }
  .catalogue-page {
    position: absolute;
    left: 233px; top: 0;
    width: 734px; height: 517px;
    background: var(--paper);
  }
  .brand {
    position: absolute;
    top: 34px; left: 0; width: 100%;
    display: flex; justify-content: center; align-items: center; gap: 8px;
  }
  .brand-mark { width: 10px; height: 10px; background: var(--ink); }
  .brand-name {
    font-weight: 700; font-size: 26px; letter-spacing: 2px; color: var(--ink);
  }
  .header-rule {
    position: absolute; top: 92px; left: 2px; right: 9px;
    height: 3px; background: var(--rule);
  }
  .product-table {
    position: absolute; left: 27px; top: 98px; width: 653px;
  }
  .table-row {
    display: grid;
    grid-template-columns: 134px 92px 51px 31px 42px 79px 82px 142px;
  }
  .table-head { height: 26px; align-items: center; }
  .table-head span {
    text-align: center; font-weight: 600; font-size: 9.5px; text-transform: uppercase;
  }
  .table-head .range-label {
    background: var(--label-bg); height: 100%;
    display: flex; align-items: center; justify-content: center;
    text-transform: none; font-size: 10px;
  }
  .table-head .range-label + span { text-transform: uppercase; }
  .product-row {
    height: 90px;
    border-bottom: 1px dashed var(--dash);
  }
  .product-row > div {
    border-left: 1px dashed var(--dash);
    display: flex; align-items: center; justify-content: center;
    text-align: center; font-size: 8.5px; font-weight: 600; line-height: 1.25;
    padding: 0 3px;
  }
  .product-row > div:first-child { border-left: none; }
  .product-row > div.cell-model { border-left: 1px dashed var(--dash); }
  .product-photo {
    width: 104px; height: 68px; border-radius: 6px;
  }
  .photo-negro { background: radial-gradient(ellipse at 50% 45%, #2b2b2b 0%, #3e3e3e 45%, #e8e8e8 75%, #fff 100%); }
  .photo-blanco { background: radial-gradient(ellipse at 50% 45%, #f3f3f3 0%, #dcdcdc 45%, #f4f4f4 75%, #fff 100%); }
  .photo-caffe { background: radial-gradient(ellipse at 50% 45%, #3a2f2b 0%, #54463f 45%, #ececec 75%, #fff 100%); }
  .photo-rojo { background: radial-gradient(ellipse at 50% 45%, #b8242c 0%, #c93a40 45%, #eee 75%, #fff 100%); }
  .cell-size { position: relative; }
  .size-drawing {
    width: 62px; height: 56px; background: var(--drawing); margin-left: -6px; margin-top: -10px;
  }
  .dim { position: absolute; font-size: 6px; font-weight: 600; }
  .dim-width { left: 10px; bottom: 16px; }
  .dim-depth { left: 46px; bottom: 8px; }
  .dim-height { right: 4px; top: 30px; transform: rotate(90deg); }
  .cell-color { flex-direction: column; gap: 6px; }
  .swatch { width: 12px; height: 12px; }
  .swatch-negro { background: var(--swatch-negro); }
  .swatch-blanco { background: var(--swatch-blanco); }
  .swatch-caffe { background: var(--swatch-caffe); }
  .swatch-rojo { background: var(--swatch-rojo); }
  .product-row > div.cell-top { align-items: flex-start; padding-top: 22px; }
  .section-title {
    position: absolute; left: 707px; top: 212px;
    transform: translate(-50%, -50%) rotate(-90deg);
    font-weight: 300; font-size: 28px; letter-spacing: 2px; color: var(--side-title);
    white-space: nowrap;
  }
  .page-number {
    position: absolute; left: 702px; top: 479px; font-size: 8px; font-weight: 600;
  }
</style>
</head>
<body>
  <main class="catalogue-page">
    <header class="brand">
      <span class="brand-mark"></span>
      <span class="brand-name">KOVARI</span>
    </header>
    <div class="header-rule"></div>

    <section class="product-table">
      <div class="table-row table-head">
        <span class="range-label">Sillones/ Armchairs</span>
        <span>Size</span><span>Color</span><span>Code</span><span>Marca</span>
        <span>Designer</span><span>Model</span><span>Finish</span>
      </div>

      <div class="table-row product-row">
        <div><div class="product-photo photo-negro" role="img" aria-label="Foto del sillón en cuero negro"></div></div>
        <div class="cell-size"><div class="size-drawing" role="img" aria-label="Diagrama de dimensiones del sillón"></div><span class="dim dim-width">80 cm</span><span class="dim dim-depth">77 cm</span><span class="dim dim-height">76 cm</span></div>
        <div class="cell-color"><span class="swatch swatch-negro"></span>Negro</div>
        <div class="cell-top">8100</div>
        <div class="cell-top">KOVARI</div>
        <div class="cell-top">Aldo Verhagen<br>1929</div>
        <div class="cell-top cell-model">Sevilla Chair</div>
        <div class="cell-top">Acero Inox. Frente C/<br>Natural, Reves C/<br>Artificial. Esponja A/D</div>
      </div>

      <div class="table-row product-row">
        <div><div class="product-photo photo-blanco" role="img" aria-label="Foto del sillón en cuero blanco"></div></div>
        <div class="cell-size"><div class="size-drawing" role="img" aria-label="Diagrama de dimensiones del sillón"></div><span class="dim dim-width">80 cm</span><span class="dim dim-depth">77 cm</span><span class="dim dim-height">76 cm</span></div>
        <div class="cell-color"><span class="swatch swatch-blanco"></span>Blanco</div>
        <div class="cell-top">8101</div>
        <div class="cell-top">KOVARI</div>
        <div class="cell-top">Aldo Verhagen<br>1929</div>
        <div class="cell-top cell-model">Sevilla Chair</div>
        <div class="cell-top">Acero Inox. Frente C/<br>Natural, Reves C/<br>Artificial. Esponja A/D</div>
      </div>

      <div class="table-row product-row">
        <div><div class="product-photo photo-caffe" role="img" aria-label="Foto del sillón en cuero café"></div></div>
        <div class="cell-size"><div class="size-drawing" role="img" aria-label="Diagrama de dimensiones del sillón"></div><span class="dim dim-width">80 cm</span><span class="dim dim-depth">77 cm</span><span class="dim dim-height">76 cm</span></div>
        <div class="cell-color"><span class="swatch swatch-caffe"></span>Caffè</div>
        <div class="cell-top">8101</div>
        <div class="cell-top">KOVARI</div>
        <div class="cell-top">Aldo Verhagen<br>1929</div>
        <div class="cell-top cell-model">Sevilla Chair</div>
        <div class="cell-top">Acero Inox. Frente C/<br>Natural, Reves C/<br>Artificial. Esponja A/D</div>
      </div>

      <div class="table-row product-row">
        <div><div class="product-photo photo-rojo" role="img" aria-label="Foto del sillón en cuero rojo"></div></div>
        <div class="cell-size"><div class="size-drawing" role="img" aria-label="Diagrama de dimensiones del sillón"></div><span class="dim dim-width">80 cm</span><span class="dim dim-depth">77 cm</span><span class="dim dim-height">76 cm</span></div>
        <div class="cell-color"><span class="swatch swatch-rojo"></span>Rojo</div>
        <div class="cell-top">8101</div>
        <div class="cell-top">KOVARI</div>
        <div class="cell-top">Aldo Verhagen<br>1929</div>
        <div class="cell-top cell-model">Sevilla Chair</div>
        <div class="cell-top">Acero Inox. Frente C/<br>Natural, Reves C/<br>Artificial. Esponja A/D</div>
      </div>
    </section>

    <div class="section-title">SILLONERIA</div>
    <div class="page-number">-1-</div>
  </main>
</body>
</html>
```